Postcard 4.25"x 6" template

We need a postcard template to send information about our wellness clinic's classes and groups.
The mailing side needs space for changeable text to talk about the clinic and brief info about our classes and groups, in addition to meeting the Federal Letter Carriage Bureau requirements for address and return address area. The return address space can be fixed with our clinic's name and address on it.
The other side should be a dynamic calendar. For the time being, please use the information listed for the month of February. However, this should be changeable so that we can update the month and the events.
Somewhere on the postcard should also be a link to our website's events page:
http://www.torvesihall.com/events
Please work with our website for guidance on the look and feel of our marketing materials.
Overall it should have a natural feel.
It needs to be able to be printed at a regular printing shop and look good. It should not require a large commercial printer.
It will also need to be editable in a Word Document format.

```html
<!DOCTYPE html>
<html lang="en">
<head>
<meta charset="utf-8">
<title>Torvesi Clinic Postcard</title>
<link href="https://fonts.googleapis.com/css2?family=Carlito:wght@400;700&family=Montserrat:wght@400;500&family=Cambo&display=swap" rel="stylesheet">
<style>
  :root {
    --page: #ffffff;
    --green-light: #f4f9ef;
    --green-mid: #d3e8c2;
    --green-deep: #a6d083;
    --brand-text: #6f7d60;
    --brand-dot: #6cbb45;
    --ink: #3b3b3b;
    --ink-soft: #555a52;
    --editable: #8d2b22;
    --cal-head: #ddd6bf;
    --cal-event: #8a7d50;
    --cal-line: #1f1f1f;
    --rule: #ffffff;
    --petal: #dcd9e6;
    --seed: #c98a2e;
  }
  * { box-sizing: border-box; margin: 0; padding: 0; }
  html, body { width: 1200px; height: 1000px; overflow: hidden; background: var(--page); }
  body { position: relative; font-family: "Carlito", "Calibri", sans-serif; }

  .card {
    position: absolute; left: 320px; width: 606px; height: 433px; overflow: hidden;
    background: linear-gradient(160deg, var(--page) 0%, var(--green-light) 28%, var(--green-mid) 62%, var(--green-deep) 100%);
    box-shadow: 0 1px 4px rgba(0,0,0,0.35);
  }
  .card--front { top: 40px; }
  .card--back { top: 515px; }

  .photo { position: absolute; }
  .photo--blossom {
    left: 320px; top: 0; width: 260px; height: 110px;
    background: radial-gradient(ellipse at 40% 25%, var(--petal) 0%, #c3c6b0 35%, rgba(111,143,74,0.45) 65%, rgba(255,255,255,0) 100%);
  }
  .photo--daisy {
    left: 320px; top: 270px; width: 286px; height: 163px;
    clip-path: polygon(0 100%, 0 80%, 100% 0, 100% 100%);
    background: linear-gradient(100deg, #c98a2e 0%, #b57a2a 45%, #d9d9d4 62%, #bdbdb8 100%);
  }

  .rules { position: absolute; left: 0; top: 0; }

  .brand { position: absolute; display: flex; align-items: center; gap: 8px; }
  .brand__dot { width: 24px; height: 24px; border-radius: 50%; background: var(--brand-dot); }
  .brand__name {
    font-family: "Carlito", sans-serif; font-size: 24px; color: var(--brand-text);
    letter-spacing: 0.5px; line-height: 1;
  }
  .card--front .brand { left: 28px; top: 62px; }
  .card--back .brand { left: 30px; top: 72px; }

  .section-title {
    position: absolute; left: 60px; top: 101px; font-weight: 400;
    font-family: "Montserrat", sans-serif; font-size: 11px; letter-spacing: 1.6px; color: var(--ink);
  }

  .intro {
    position: absolute; left: 68px; top: 192px; width: 150px;
    font-size: 12px; line-height: 15.6px; text-align: center; color: var(--ink);
  }

  .web { position: absolute; font-family: "Montserrat", sans-serif; color: var(--ink-soft); }
  .card--front .web { left: 12px; top: 410px; font-size: 12px; letter-spacing: 2.4px; }
  .card--back .web { right: 17px; top: 402px; font-size: 9.5px; letter-spacing: 2px; }

  .calendar { position: absolute; left: 305px; top: 76px; width: 267px; }
  .calendar__month {
    font-family: "Cambo", serif; font-size: 18px; text-align: center; color: #111;
    letter-spacing: 0.5px; line-height: 22px;
  }
  .calendar__grid { width: 267px; border-collapse: collapse; table-layout: fixed; }
  .calendar__grid th, .calendar__grid td { border: 1.5px solid var(--cal-line); }
  .calendar__grid th { background: var(--cal-head); font-size: 9px; font-weight: 700; height: 16px; color: #222; }
  .calendar__grid td {
    background: rgba(255,255,255,0.25); vertical-align: top; text-align: right;
    font-size: 7px; padding: 2px 2px 0; color: #222; position: relative;
  }
  .row--short td { height: 34px; }
  .row--tall td { height: 139px; }
  .row--week td { height: 36px; }
  .event {
    position: absolute; left: 5px; right: 5px; top: 9px; bottom: 2px;
    background: var(--cal-event); text-align: left; color: #fff;
    font-size: 5.8px; line-height: 7.4px; padding: 3px 3px;
  }
  .event__item + .event__item { border-top: 1px solid #fff; margin-top: 4px; padding-top: 4px; }

  .editable {
    position: absolute; left: 47px; top: 163px; list-style: none;
    font-size: 14.5px; line-height: 22px; color: var(--editable);
  }

  .return-address {
    position: absolute; left: 35px; top: 325px; font-family: "Montserrat", sans-serif; font-style: normal;
    font-size: 11.5px; line-height: 15px; color: var(--ink);
  }
  .contact {
    position: absolute; left: 35px; top: 387px; font-family: "Montserrat", sans-serif;
    font-size: 11.5px; line-height: 15.5px; color: var(--ink);
  }
  .divider { position: absolute; background: var(--rule); }
  .divider--return { left: 23px; top: 377px; width: 268px; height: 2px; }
  .divider--stamp { left: 339px; top: 42px; width: 2px; height: 336px; }
  .address-line { position: absolute; left: 355px; width: 222px; height: 2px; background: var(--rule); }
</style>
</head>
<body>

<section class="card card--front" aria-label="Calendar side">
  <div class="photo photo--blossom" role="img" aria-label="Photograph of a passion flower blossom with leaves"></div>
  <div class="photo photo--daisy" role="img" aria-label="Close-up photograph of a white daisy with an orange centre"></div>

  <svg class="rules" width="606" height="433" viewBox="0 0 606 433" aria-hidden="true">
    <g stroke="#ffffff" stroke-width="2" fill="none">
      <line x1="0" y1="214" x2="606" y2="52"/>
      <line x1="310" y1="0" x2="245" y2="433"/>
      <line x1="278" y1="0" x2="298" y2="433"/>
      <line x1="0" y1="400" x2="606" y2="300"/>
      <line x1="120" y1="433" x2="330" y2="0"/>
      <line x1="606" y1="270" x2="470" y2="433"/>
    </g>
  </svg>

  <div class="brand">
    <span class="brand__dot"></span>
    <span class="brand__name">TORVESI CLINIC</span>
  </div>
  <h2 class="section-title">Classes and Groups</h2>

  <p class="intro">The Torvesi Clinic brings holistic, natural and integrative care to the front of the mental health field. Our therapies include naturopathy, biofeedback, acupuncture, medication management, medication tapering and discontinuation, psychotherapy, nutritional therapy, herbal and Chinese herbal medicine, and homeopathy.</p>

  <div class="calendar">
    <h3 class="calendar__month">FEBRUARY 2014</h3>
    <table class="calendar__grid">
      <colgroup>
        <col style="width:33px"><col style="width:56px"><col style="width:31px"><col style="width:58px"><col style="width:32px"><col style="width:25px"><col style="width:32px">
      </colgroup>
      <thead>
        <tr><th>Sun</th><th>Mon</th><th>Tue</th><th>Wed</th><th>Thu</th><th>Fri</th><th>Sat</th></tr>
      </thead>
      <tbody>
        <tr class="row--short"><td></td><td></td><td></td><td></td><td></td><td></td><td>1</td></tr>
        <tr class="row--tall">
          <td>2</td>
          <td>3
            <div class="event">
              <p class="event__item">Group IV Session<br>Group Acupuncture</p>
              <p class="event__item">Group Acupuncture with Mara Ellison</p>
            </div>
          </td>
          <td>4</td>
          <td>5
            <div class="event">
              <p class="event__item">Yoga After Trauma: Reclaiming the Body and Mind<br>"Happy Hour" Group Acupuncture</p>
              <p class="event__item">Healing From Trauma and Addiction</p>
            </div>
          </td>
          <td>6</td><td>7</td><td>8</td>
        </tr>
        <tr class="row--short"><td>9</td><td>10</td><td>11</td><td>12</td><td>13</td><td>14</td><td>15</td></tr>
        <tr class="row--week"><td>16</td><td>17</td><td>18</td><td>19</td><td>20</td><td>21</td><td>22</td></tr>
        <tr class="row--week"><td>23</td><td>24</td><td>25</td><td>26</td><td>27</td><td>28</td><td></td></tr>
      </tbody>
    </table>
  </div>

  <p class="web">http://www.torvesihall.com/events</p>
</section>

<section class="card card--back" aria-label="Mailing side">
  <div class="brand">
    <span class="brand__dot"></span>
    <span class="brand__name">TORVESI CLINIC</span>
  </div>

  <ul class="editable">
    <li>You can edit this text box.</li>
    <li>You can edit this text box.</li>
    <li>You can edit this text box.</li>
    <li>You can edit this text box.</li>
    <li>You can edit this text box.</li>
  </ul>

  <address class="return-address">528 NE Alder Lane<br>Cedarton,<br>Oregon 97000</address>
  <div class="divider divider--return"></div>
  <p class="contact">Phone: (555) 014-2270<br>Fax: (555) 014-3391</p>

  <div class="divider divider--stamp"></div>
  <div class="address-line" style="top:196px"></div>
  <div class="address-line" style="top:220px"></div>
  <div class="address-line" style="top:244px"></div>
  <div class="address-line" style="top:268px"></div>

  <p class="web">http://www.torvesihall.com/events</p>
</section>

</body>
</html>
```